Hire OKRIM

We are developing a website that allows Hospitality employees to apply for hospitality jobs in the OKRIM union. They do this by completing a standarized application form.

The wirefram lays out all of the pages and how they are conected.

The focus is on functinality, simplicity and intuitive.

The site will be in Thai and English.

We're looking for a mok up the first page only to evaluate designs. If we're able to find a design that works, we would ask for the all pages of the wireframe to be completed as per the alocated budget.

Thanks to all the designers for the initial landing pagedesign.  We have committed topayment for a finished design of all 11 pages and windows as per our attachedwireframe.  We would like to choosea final designer by Monday the 7th.x

Reason: We have committed to payment for a finished design of all 11 pages and windows as per our attached wireframe. We would like to choose a final designer by Monday the 7th.

Target Market(s)

Thai nationals ages 20-30 that work in the hospitality industry.

Industry/Entity Type

Hospitality

Colors

Designer to choose colors to be used in the design.

Requirements
Must have
• Intuitive layout
Simple and clean - no redundancy.

```html
<!DOCTYPE html>
<html lang="en">
<head>
<meta charset="utf-8">
<title>Hire OKRIM</title>
<link href="https://fonts.googleapis.com/css2?family=Open+Sans:wght@400;600&family=Sarabun:wght@400&display=swap" rel="stylesheet">
<style>
:root{
  --green:#8cc63f;
  --green-dark:#5a8a1e;
  --ink:#333;
  --soft:#999;
  --line:#dcdcdc;
  --footer:#efefef;
  --white:#fff;
  --black:#1c1c1c;
}
*{box-sizing:border-box;margin:0;padding:0}
html,body{width:766px;height:1200px;overflow:hidden;background:var(--white)}
body{position:relative;font-family:"Open Sans",Arial,sans-serif;color:var(--ink)}
.abs{position:absolute}
h2,h3{font-weight:400}

/* header */
.site-header{position:absolute;left:0;top:0;width:766px;height:70px;background:var(--white)}
.brand{left:64px;top:14px;display:flex;align-items:center;gap:8px}
.brand-mark{width:44px;height:44px;background:var(--green);border-radius:4px}
.brand-name{font-size:26px;font-weight:400;color:var(--green-dark);letter-spacing:.5px;white-space:nowrap}
.lang{left:398px;top:32px;font-family:"Sarabun",sans-serif;font-size:13px;line-height:16px;color:#888;white-space:nowrap}
.flag{top:34px;width:15px;height:10px;border:1px solid #ccc}
.flag-en{left:498px;background:#2c3f7a}
.flag-th{left:519px;background:linear-gradient(#c8102e 0 18%,#fff 18% 34%,#2d2a4a 34% 66%,#fff 66% 82%,#c8102e 82%)}
.btn-top{top:30px;height:20px;font-size:8.5px;font-weight:600;line-height:20px;color:var(--white);white-space:nowrap;text-align:center;border-radius:2px}
.btn-contact{left:555px;width:77px;background:#3c3c3c}
.btn-login{left:636px;width:42px;background:var(--green)}
.social-square{left:682px;top:29px;width:21px;height:21px;background:#3b5998;border-radius:3px}

/* hero */
.hero{position:absolute;left:0;top:70px;width:766px;height:343px}
.hero-half{position:absolute;top:0;height:343px}
.hero-seek{left:0;width:383px;background:linear-gradient(120deg,#9cb85a,#8aaa3c 50%,#7e9c34)}
.hero-hire{left:383px;width:383px;background:linear-gradient(120deg,#5a5a5a,#474747 55%,#3c3c3c)}
.hero h2{position:absolute;top:38px;font-size:24px;line-height:30px;color:var(--white);white-space:nowrap}
.field-label{position:absolute;font-size:10px;line-height:13px;color:var(--white);white-space:nowrap}
.field{position:absolute;width:160px;height:26px;background:var(--white);border-radius:2px;font-size:8px;color:var(--soft);padding:0 10px;display:flex;align-items:center}
.field-select::after{content:"";position:absolute;right:6px;top:11px;border:4px solid transparent;border-top-color:#aaa}
.field-select::before{content:"";position:absolute;right:20px;top:6px;width:1px;height:14px;background:#ddd}
.signup{position:absolute;top:260px;width:92px;height:30px;font-size:11px;font-weight:600;white-space:nowrap;display:flex;align-items:center;justify-content:center;border-radius:2px}
.signup-dark{background:var(--black);color:var(--white)}
.signup-green{background:var(--green);color:#1e2a0c}

/* stories */
.section-title{position:absolute;font-size:14px;line-height:18px;color:var(--green-dark)}
.story-photo{position:absolute;left:66px;width:147px;height:92px}
.story-title{position:absolute;left:226px;font-size:12px;line-height:15px;color:#444}
.story-meta{position:absolute;left:226px;font-size:7.5px;line-height:10px;color:var(--soft);white-space:nowrap}
.story-text{position:absolute;left:226px;width:200px;font-size:7.5px;line-height:12px;color:#666}
.people-art{left:484px;top:456px;width:176px;height:324px;background:linear-gradient(#e8e8e8,#cfcfcf);border-radius:6px}
.rule{position:absolute;left:64px;width:639px;height:1px;background:var(--line)}

/* feature videos */
.feature-title{position:absolute;top:834px;font-size:13.5px;line-height:18px;color:var(--green-dark);white-space:nowrap}
.feature-media{position:absolute;top:858px;width:200px;height:100px}
.play{position:absolute;left:86px;top:36px;width:28px;height:28px;border-radius:50%;background:rgba(255,255,255,.75);border:2px solid rgba(90,90,90,.5)}
.play::after{content:"";position:absolute;left:10px;top:7px;border:6px solid transparent;border-left:9px solid #555;border-right:0}
.feature-sub{position:absolute;top:966px;font-size:10.5px;line-height:14px;color:var(--green-dark);white-space:nowrap}
.feature-text{position:absolute;top:983px;width:200px;font-size:7.5px;line-height:11.5px;color:#777}

/* partners */
.partners{position:absolute;left:64px;top:1076px;width:639px;display:flex;justify-content:space-between;align-items:center}
.partner{font-size:13px;font-weight:600;color:#666;white-space:nowrap}

/* footer */
.site-footer{position:absolute;left:0;top:1128px;width:766px;height:72px;background:var(--footer)}
.foot-links{left:64px;top:19px;font-size:8.5px;line-height:12px;color:#555;white-space:nowrap}
.foot-copy{left:64px;top:37px;font-size:8px;line-height:12px;color:#666;white-space:nowrap}
.foot-social{top:28px;width:16px;height:16px;border-radius:50%;background:#9a9a9a}
</style>
</head>
<body>

<header class="site-header">
  <div class="abs brand"><span class="brand-mark"></span><span class="brand-name">Hire OKRIM</span></div>
  <div class="abs lang">ภาษาไทยคลิกที่นี่</div>
  <span class="abs flag flag-en"></span>
  <span class="abs flag flag-th"></span>
  <div class="abs btn-top btn-contact">CONTACT OKRIM</div>
  <div class="abs btn-top btn-login">LOG IN</div>
  <span class="abs social-square"></span>
</header>

<section class="hero">
  <div class="hero-half hero-seek" role="img" aria-label="Photo of a young woman relaxing on a sofa, tinted green">
    <h2 style="left:142px">I Want a Job</h2>
    <div class="field-label" style="left:143px;top:80px">I am</div>
    <div class="field" style="left:143px;top:96px">Name</div>
    <div class="field-label" style="left:143px;top:140px">My E-mail id</div>
    <div class="field" style="left:143px;top:156px">E-mail</div>
    <div class="field-label" style="left:143px;top:200px">Password</div>
    <div class="field" style="left:143px;top:216px">Enter here</div>
    <div class="signup signup-dark" style="left:210px">SIGN UP NOW</div>
  </div>
  <div class="hero-half hero-hire" role="img" aria-label="Photo of a businessman working on a laptop, tinted grey">
    <h2 style="left:79px">We Want Staff</h2>
    <div class="field-label" style="left:80px;top:80px">We are</div>
    <div class="field" style="left:80px;top:96px">Company Name</div>
    <div class="field-label" style="left:80px;top:140px">Our E-mail id</div>
    <div class="field" style="left:80px;top:156px">E-mail</div>
    <div class="field-label" style="left:80px;top:200px">Password</div>
    <div class="field field-select" style="left:80px;top:216px">Enter here</div>
    <div class="signup signup-green" style="left:147px">SIGN UP NOW</div>
  </div>
</section>

<h3 class="section-title" style="left:64px;top:440px">Mauris tempor risus</h3>

<div class="story-photo" style="top:474px;background:linear-gradient(135deg,#cfdbe6,#eef2f5)" role="img" aria-label="Photo of a businesswoman at a desk with a laptop"></div>
<div class="story-title" style="top:475px">Maecenas sed</div>
<div class="story-meta" style="top:493px">By Dana Reed &nbsp;/&nbsp; Layout, Print, Design</div>
<p class="story-text" style="top:506px">Aliquam vitae mauris non lacus malesuada vestibu-lum. Aenean gravida ut purus non fringilla. In tinci-dunt odio a sodales euismod. In faucibus sapien enim, eu congue velit condimentum</p>

<div class="story-photo" style="top:581px;background:linear-gradient(135deg,#d9dde0,#b9c0c6)" role="img" aria-label="Photo of a smiling woman holding a folder in an office"></div>
<div class="story-title" style="top:582px">Maecenas sed</div>
<div class="story-meta" style="top:600px">By Dana Reed &nbsp;/&nbsp; Layout, Print, Design</div>
<p class="story-text" style="top:613px">Aliquam vitae mauris non lacus malesuada vestibu-lum. Aenean gravida ut purus non fringilla. In tinci-dunt odio a sodales euismod. In faucibus sapien enim, eu congue velit condimentum</p>

<div class="story-photo" style="top:688px;background:linear-gradient(135deg,#c6d7e6,#e6edf3)" role="img" aria-label="Photo of a smiling senior businessman"></div>
<div class="story-title" style="top:689px">Maecenas sed</div>
<div class="story-meta" style="top:707px">By Dana Reed &nbsp;/&nbsp; Layout, Print, Design</div>
<p class="story-text" style="top:720px">Aliquam vitae mauris non lacus malesuada vestibu-lum. Aenean gravida ut purus non fringilla. In tinci-dunt odio a sodales euismod. In faucibus sapien enim, eu congue velit condimentum</p>

<div class="abs people-art" role="img" aria-label="Illustration of a businessman and businesswoman in grey suits"></div>

<div class="rule" style="top:806px"></div>

<h3 class="feature-title" style="left:70px">Etiam vehicula</h3>
<div class="feature-media" style="left:70px;background:linear-gradient(#9fb0c4,#6d7d8e)" role="img" aria-label="Video still of an office building"><span class="play"></span></div>
<div class="feature-sub" style="left:70px">Maecenas sed lacus pellentesque</div>
<p class="feature-text" style="left:70px">Nullam cursus eros est, non fringilla lectus consect etur et. Maecenas dapibus massa ut sem fermentum tristique pulvinar vitae mattis.</p>

<h3 class="feature-title" style="left:284px">Proin at tortor</h3>
<div class="feature-media" style="left:284px;background:linear-gradient(#e2e0da,#b9b5ac)" role="img" aria-label="Video still of a magnifying glass over job listings"><span class="play"></span></div>
<div class="feature-sub" style="left:284px">Maecenas sed lacus pellentesque</div>
<p class="feature-text" style="left:284px">Nullam cursus eros est, non fringilla lectus consect etur et. Maecenas dapibus massa ut sem fermentum tristique pulvinar vitae mattis.</p>

<h3 class="feature-title" style="left:497px">Donec nunc mauris</h3>
<div class="feature-media" style="left:497px;background:linear-gradient(#8a6a3c,#3e3024)" role="img" aria-label="Video still of a man thinking at a laptop"><span class="play"></span></div>
<div class="feature-sub" style="left:497px">Maecenas sed lacus pellentesque</div>
<p class="feature-text" style="left:497px">Nullam cursus eros est, non fringilla lectus consect etur et. Maecenas dapibus massa ut sem fermentum tristique pulvinar vitae mattis.</p>

<div class="rule" style="top:1054px"></div>

<div class="partners">
  <span class="partner">Fernhall</span>
  <span class="partner">Lumora</span>
  <span class="partner">Trellis</span>
  <span class="partner">Brandwick</span>
  <span class="partner">Koriva</span>
  <span class="partner">Altmere</span>
  <span class="partner">Nexbay</span>
  <span class="partner">Pellan</span>
  <span class="partner">Corvix</span>
</div>

<footer class="site-footer">
  <div class="abs foot-links">Home &nbsp;|&nbsp; Who we are &nbsp;|&nbsp; Contact</div>
  <div class="abs foot-copy">Copyright © 2014 &nbsp;Hire OKRIM. &nbsp;All rights reserved.</div>
  <span class="abs foot-social" style="left:619px"></span>
  <span class="abs foot-social" style="left:642px"></span>
  <span class="abs foot-social" style="left:664px"></span>
  <span class="abs foot-social" style="left:687px"></span>
</footer>

</body>
</html>
```